MEDITERRANEAN Cafe Website needed

We are a MEDITERRANEAN Café serving Coffee, breakfast, Pizza, Pasta, Sandwiches etc.

We need a home page, menu & venue, Reservations & Events, Delivery
Connect (Social media / Feedback / Contact us),Join our team
Updates

Can we keep the designs in Mediterranean colours, look, and feel pleasethanks Added Saturday, December 10, 2016

Project Deadline Extended Reason: I have guarantied the payment and upgraded the project. I would like this would to give more time for new designs to come in and a couple of potential designs to show more. Added Sunday, December 11, 2016

Industry/Entity Type

Cafe

Coding

Coded - Design and coding required

Number of Pages Required

5+ page

Requirements
Must have
• MEDITERRANEAN feel, colours, style etc.
• http://www.corvanetta (DOT) co (DOT) uk
Nice to have

```html
<!DOCTYPE html>
<html lang="en">
<head>
<meta charset="utf-8">
<title>Solenza Café</title>
<link href="https://fonts.googleapis.com/css2?family=Open+Sans:wght@300;400;600;700&display=swap" rel="stylesheet">
<style>
:root{
  --wine:#3d0a0c;
  --wine-deep:#240405;
  --red:#c8171d;
  --red-dark:#a31015;
  --cream:#fdf6c9;
  --ink:#222;
  --white:#fff;
  --photo-warm:#6b2a1c;
}
*{box-sizing:border-box;margin:0;padding:0}
html,body{width:1200px;height:5056px;overflow:hidden}
body{position:relative;font-family:"Open Sans",Arial,sans-serif;color:var(--ink);background:var(--wine)}
.abs{position:absolute}
.center{text-align:center}

/* hero */
.hero{left:0;top:0;width:1200px;height:883px;background:radial-gradient(ellipse at 50% 45%,#5a1214 0%,var(--wine) 55%,var(--wine-deep) 100%)}
.search{left:68px;top:34px;width:278px;height:34px;border:2px solid var(--white);border-radius:4px;color:var(--white);font-size:15px;font-weight:600;padding:6px 12px}
.search svg{position:absolute;right:10px;top:6px}
.top-btn{top:34px;height:34px;border:2px solid var(--white);border-radius:4px;color:var(--white);font-size:13px;font-weight:600;line-height:30px;text-align:center}
.brand{left:470px;top:90px;width:260px;height:220px;border-radius:50%;background:var(--red);color:var(--white);display:flex;align-items:center;justify-content:center;font-size:40px;font-weight:700}
.hero-photo{left:320px;top:300px;width:560px;height:490px;border-radius:50%;background:radial-gradient(circle at 45% 45%,#e8a23c 0%,#c46a22 55%,#7a3a14 100%)}
.arrow{top:560px}
.dots{left:525px;top:838px;display:flex;gap:14px}
.dots span{width:15px;height:15px;border-radius:50%;background:#111}
.dots span:first-child{background:var(--white)}

/* nav band */
.nav-band{left:135px;top:883px;width:930px;height:145px;background:var(--red)}
.social-line{left:230px;top:50px;width:600px;height:2px;background:var(--white)}
.social-dot{top:22px;width:58px;height:58px;border:3px solid var(--white);border-radius:50%;background:var(--red)}
.nav{left:0;top:106px;width:930px;display:flex;justify-content:space-around;padding:0 60px;color:var(--white);font-size:16px;font-weight:600}

/* story */
.story-cream{left:0;top:1028px;width:1200px;height:490px;background:var(--cream)}
.story-dark{left:0;top:1518px;width:1200px;height:335px;background:var(--wine-deep)}
.story-card{left:135px;top:1028px;width:930px;height:825px;background:var(--cream)}
.pasta{left:200px;top:20px;width:530px;height:420px;border-radius:50%;background:radial-gradient(ellipse,#f5d35a 0%,#e8b534 60%,rgba(253,246,201,0) 72%)}
.h-title{font-weight:300;font-size:72px;color:#1a1a1a;line-height:1}
.story-title{left:0;top:500px;width:930px}
.body-text{font-size:15px;line-height:24px;color:#333}
.story-text{left:30px;top:615px;width:870px}
.read-more{font-size:15px;font-weight:700;color:var(--red)}

/* menus */
.menus{left:0;top:1853px;width:1200px;height:698px;background:linear-gradient(180deg,#4d1a12 0%,#3a120c 50%,#2c0c08 100%)}
.menu-card{top:260px;height:374px;border:2px solid rgba(255,255,255,.7);color:var(--white)}
.menu-badge{top:-70px;width:150px;height:150px;border-radius:50%;background:var(--red-dark);color:var(--white);font-size:24px;font-weight:600;display:flex;align-items:flex-end;justify-content:center;padding-bottom:30px}
.menu-price{top:140px;width:100%;font-size:22px;font-weight:700;line-height:1.3}
.menu-price b{font-size:44px}
.menu-link{bottom:28px;width:100%;font-size:15px}

/* team */
.team{left:0;top:2551px;width:1200px;height:795px;background:var(--cream)}
.team-title{left:0;top:140px;width:1200px}
.team-text{left:130px;top:240px;width:940px}
.portrait{top:434px;width:212px;height:212px;border-radius:50%;border:4px solid var(--white);box-shadow:0 0 0 2px #bbb;background:radial-gradient(circle at 50% 40%,#d9c2a8 0%,#b5a08a 60%,#e9e9e9 100%)}
.member{top:686px;width:300px;color:var(--red);font-weight:700;font-size:16px}

/* reserve */
.reserve{left:0;top:3346px;width:1200px;height:450px;background:var(--wine-deep)}
.reserve-title{left:0;top:92px;width:1200px;color:var(--white);font-size:64px;font-weight:400}
.reserve-sub{left:0;top:170px;width:1200px;color:var(--white);font-size:30px;font-weight:300}
.field{height:44px;border:2px solid rgba(255,255,255,.8);border-radius:4px;background:#000;color:var(--white);font-size:14px;padding:10px 10px}
.btn-red{background:var(--red);color:var(--white);font-weight:600;font-size:15px;text-align:center;border-radius:4px}

/* events */
.events-band{left:135px;top:3795px;width:930px;height:182px;background:var(--red);color:var(--white)}
.events-title{left:0;top:55px;width:930px;font-size:68px;font-weight:300;line-height:1}
.events-sub{left:0;top:138px;width:930px;font-size:28px;font-weight:300}
.events{left:0;top:3977px;width:1200px;height:640px;background:var(--cream)}
.burger{left:152px;top:35px;width:455px;height:405px;border-radius:48%;background:radial-gradient(ellipse,#c9702f 0%,#8a3b1c 55%,rgba(253,246,201,0) 72%)}
.bullet{left:640px;width:20px;height:20px;border-radius:50%;background:var(--red)}
.bullet-text{left:675px;width:370px;font-size:15px;line-height:22px}
.see-all{left:916px;top:424px;width:122px;height:34px;border:2px solid var(--red);color:var(--red);font-size:13px;text-align:center;line-height:30px}

/* footer */
.footer{left:0;top:4617px;width:1200px;height:388px;background:var(--wine-deep);color:var(--white)}
.footer h3{font-size:30px;font-weight:600}
.soc{top:303px;width:34px;height:34px;border-radius:50%;background:var(--white)}
.foot-field{left:768px;width:272px;height:46px;background:#000;border:1px solid #555;color:var(--white);font-size:14px;padding:12px 12px}
.bottom-bar{left:0;top:5005px;width:1200px;height:51px;background:#150203;color:var(--white);font-size:14px;font-weight:700;text-align:center;line-height:51px}
</style>
</head>
<body>

<section class="abs hero">
  <div class="abs search">SEARCH FOOD
    <svg width="20" height="20" viewBox="0 0 20 20"><circle cx="8" cy="8" r="6" fill="none" stroke="#fff" stroke-width="2.5"/><line x1="12.5" y1="12.5" x2="18" y2="18" stroke="#fff" stroke-width="3"/></svg>
  </div>
  <div class="abs top-btn" style="left:884px;width:110px">JOIN NOW</div>
  <div class="abs top-btn" style="left:1004px;width:130px">RESERVATIONS</div>
  <div class="abs brand">Solenza</div>
  <div class="abs hero-photo" role="img" aria-label="Pizza on a wooden serving board"></div>
  <svg class="abs arrow" style="left:26px" width="24" height="44" viewBox="0 0 24 44"><polyline points="20,4 4,22 20,40" fill="none" stroke="#fff" stroke-width="6"/></svg>
  <svg class="abs arrow" style="left:1150px" width="24" height="44" viewBox="0 0 24 44"><polyline points="4,4 20,22 4,40" fill="none" stroke="#fff" stroke-width="6"/></svg>
  <div class="abs dots"><span></span><span></span><span></span><span></span><span></span></div>
</section>

<nav class="abs nav-band">
  <div class="abs social-line"></div>
  <div class="abs social-dot" style="left:200px"></div>
  <div class="abs social-dot" style="left:360px"></div>
  <div class="abs social-dot" style="left:520px"></div>
  <div class="abs social-dot" style="left:680px"></div>
  <div class="abs nav"><span>Home</span><span>About US</span><span>Our Story</span><span>Our Team</span><span>Menu</span><span>Events</span><span>Contact us</span></div>
</nav>

<div class="abs story-cream"></div>
<div class="abs story-dark"></div>
<section class="abs story-card">
  <div class="abs pasta" role="img" aria-label="Nests of tagliatelle pasta with parsley"></div>
  <h2 class="abs h-title story-title center">Our Story</h2>
  <p class="abs body-text story-text center">An early morning walk to the bakery around the corner is a way of life in the Mediterranean. Nothing beats the first batch of bread from the oven to start your day. Solenza Café started with a simple idea: we wanted people to experience that taste all the time. So we combined a variety of best ingredients and delicacies to make you that healthy stuffed pita to enjoy the way you like, whenever you get the urge to do so. As time went by we opened our hearts and ears to our customers and added a range of fresh and delicious products to our menu – salads, traditional Mediterranean starters, desserts – and we made sure you don't miss out on the great morning lattes.</p>
  <p class="abs read-more center" style="left:0;top:790px;width:930px">Read More</p>
</section>

<section class="abs menus" role="img" aria-label="Dark background photo of Mediterranean dishes">
  <div class="abs menu-card" style="left:135px;width:330px">
    <div class="abs menu-badge" style="left:88px">BREAKFAST</div>
    <p class="abs menu-price center">FROM<br>£<b>4.75</b></p>
    <p class="abs menu-link center">View Menu</p>
  </div>
  <div class="abs menu-card" style="left:455px;width:293px">
    <div class="abs menu-badge" style="left:70px">LUNCH</div>
    <p class="abs menu-price center">FROM<br>£<b>6.95</b></p>
    <p class="abs menu-link center">View Menu</p>
  </div>
  <div class="abs menu-card" style="left:768px;width:297px">
    <div class="abs menu-badge" style="left:72px">MAIN MENU</div>
    <p class="abs menu-price center" style="font-size:20px;top:150px">ENJOY THE TASTE<br>OF ITALY</p>
    <p class="abs menu-link center">View Menu</p>
  </div>
</section>

<section class="abs team">
  <h2 class="abs h-title team-title center">Our Team</h2>
  <div class="abs body-text team-text center">
    <p>One of the centerpieces and the Mediterranean symbol of Solenza Café are its colors which inspire a carefree wave, and an invitation to relax in that particular world of Solenza Café. The mixture of captivating marina view and fresh ingredients is played in perfect harmony with the restaurant's atmosphere.</p>
    <p style="margin-top:12px">Our team has a great sense of pride in everything we do and a passion to ensure you have an incredible experience every time.</p>
    <p class="read-more" style="margin-top:16px">Read More</p>
  </div>
  <svg class="abs" style="left:18px;top:522px" width="22" height="40" viewBox="0 0 22 40"><polyline points="18,4 4,20 18,36" fill="none" stroke="#fff" stroke-width="5"/></svg>
  <svg class="abs" style="left:1162px;top:522px" width="22" height="40" viewBox="0 0 22 40"><polyline points="4,4 18,20 4,36" fill="none" stroke="#fff" stroke-width="5"/></svg>
  <div class="abs portrait" style="left:137px" role="img" aria-label="Portrait of team member Marco Dellan"></div>
  <div class="abs portrait" style="left:494px" role="img" aria-label="Portrait of team member Luca Ferrant"></div>
  <div class="abs portrait" style="left:851px" role="img" aria-label="Portrait of team member Nico Sarvelli"></div>
  <p class="abs member center" style="left:93px">MARCO DELLAN</p>
  <p class="abs member center" style="left:450px">LUCA FERRANT</p>
  <p class="abs member center" style="left:807px">NICO SARVELLI</p>
</section>

<section class="abs reserve">
  <h2 class="abs reserve-title center">Reserve Now</h2>
  <p class="abs reserve-sub center">EVERY GUEST IS SPECIAL HERE</p>
  <div class="abs field" style="left:135px;top:288px;width:252px">Name</div>
  <div class="abs field" style="left:473px;top:288px;width:252px">Date</div>
  <div class="abs field" style="left:813px;top:288px;width:252px">Person</div>
  <div class="abs field" style="left:135px;top:356px;width:252px">E-Mail</div>
  <div class="abs field" style="left:473px;top:356px;width:252px">Time</div>
  <div class="abs btn-red" style="left:813px;top:356px;width:252px;height:44px;line-height:44px">MAKE A Reservations</div>
</section>

<div class="abs events-band">
  <h2 class="abs events-title center">Events</h2>
  <p class="abs events-sub center">JOIN US FOR SOMETHING SPECIAL</p>
</div>
<section class="abs events">
  <div class="abs burger" role="img" aria-label="Gourmet burger with tomato and rocket"></div>
  <div class="abs bullet" style="top:153px"></div>
  <p class="abs bullet-text" style="top:140px">All of your Solenza Café favorites are available, just right, easily and affordable.</p>
  <div class="abs bullet" style="top:248px"></div>
  <p class="abs bullet-text" style="top:235px">Turn any large party or event into a Solenza Café celebration.</p>
  <div class="abs bullet" style="top:339px"></div>
  <p class="abs bullet-text" style="top:326px">We will gladly honor requests to modify orders to suit specific health or dietary needs.</p>
  <div class="abs see-all">SEE ALL EVENTS</div>
  <p class="abs body-text" style="left:165px;top:466px;width:440px;font-size:14px;line-height:21px">Be it an intimate gathering of friends, a celebration of a corporate milestone, or an engagement reception, Solenza Café is the perfect venue. Reserve with us and let us be your host to a true event.</p>
  <p class="abs read-more" style="left:165px;top:548px">Read More</p>
</section>

<footer class="abs footer">
  <h3 class="abs" style="left:165px;top:22px">Location</h3>
  <p class="abs" style="left:165px;top:80px;width:480px;font-size:14px;line-height:22px">Located in Porto Lenta, Solenza Café has become a beacon for Service and Quality food. Enjoy an after-dinner coffee or drink from the spacious waterfront magical outdoors of the Marina or our comfortable indoor where you can relax and spend a memorable time with us.</p>
  <h3 class="abs" style="left:165px;top:215px">Social media</h3>
  <div class="abs soc" style="left:165px"></div>
  <div class="abs soc" style="left:213px"></div>
  <div class="abs soc" style="left:261px"></div>
  <div class="abs soc" style="left:309px"></div>
  <div class="abs soc" style="left:357px"></div>
  <div class="abs soc" style="left:405px"></div>
  <h3 class="abs" style="left:768px;top:22px">Contact us</h3>
  <div class="abs foot-field" style="top:82px">Name</div>
  <div class="abs foot-field" style="top:146px">Your Mail</div>
  <div class="abs foot-field" style="top:210px">Message</div>
  <div class="abs btn-red" style="left:768px;top:282px;width:150px;height:44px;line-height:44px;border-radius:0">SUBMIT</div>
</footer>
<div class="abs bottom-bar">© 2016 | ALL RIGHTS RESERVED</div>

</body>
</html>
```